Business Cards for Bramblewood Coatings Pty Ltd

Hi every one i need a design for my buisness cards. I Want my logo in it and the name of the company needs to stand out Bramblewood Coatings Pty Ltd. I want the background of the buisness cards black and i want the font to stand out in either a white or a silver stylish text. I want the design to be simple but original not to in your face if you know what i mean. I want on the back of the buisness cards to have the services that my buisness offers.
• Interior/Exterior
• Residential/Commercial
• Special effects/Texture Coatings
• Water Damage Repair
• Fully qualified
• Pensioner Discount
• 10 Year guarantee
• Fully Insured
• Obligation free quotes
full internal repaints include a proffesionla cleaning service
I want the services on the back to be layed out in an originall way not just dot points. If possible could my logo take up the whole back ground of the back but the text with the services be kind of like transparent so u cvan still see the logo i dont know if its possible it woiuld just look cool if possible. When i pick a design ill give my contact details to the designer to add to the design at the end. Any questions please just ask! Ill upload my logo.
Conatcs will include office phone: Mobile: E-mail - dean@bramblewoodcoatings.com.au, Ill also have a Postal address which is a PO Box and my website is www.bramblewoodcoatings.com.au

```html
<!DOCTYPE html>
<html lang="en">
<head>
<meta charset="utf-8">
<title>Bramblewood Coatings Pty Ltd – Business Cards</title>
<link rel="stylesheet" href="https://fonts.googleapis.com/css2?family=Open+Sans:wght@400;600;700;800&display=swap">
<style>
  :root {
    --page: #e9e7e3;
    --card: #2d2d2f;
    --card-edge: #242426;
    --lime: #8fd231;
    --lime-soft: rgba(143, 210, 49, 0.55);
    --white: #f4f4f4;
    --silver: #b9b9bb;
    --muted: #8b8b8e;
    --font: "Open Sans", Arial, sans-serif;
  }
  * { box-sizing: border-box; margin: 0; padding: 0; }
  html, body {
    width: 1200px; height: 900px; overflow: hidden;
    background: var(--page);
    font-family: var(--font);
  }
  .stage {
    position: relative; width: 1200px; height: 900px;
  }
  .card {
    position: absolute; left: 240px;
    width: 720px; height: 411px;
    background: radial-gradient(circle at 50% 40%, #353537 0%, var(--card) 60%, var(--card-edge) 100%);
    border-radius: 4px;
    box-shadow: 0 6px 18px rgba(0,0,0,0.25);
    overflow: hidden;
  }
  .card--back { top: 30px; }
  .card--front { top: 469px; }

  /* Brand mark: plain square + name */
  .brand { position: absolute; text-align: center; }
  .brand__square {
    display: block; margin: 0 auto;
    background: var(--lime); border-radius: 8px;
  }
  .brand__name {
    display: block; color: var(--white); font-weight: 800;
    text-transform: uppercase; letter-spacing: 0.5px; line-height: 1.15;
  }
  .card--back .brand { left: 210px; top: 88px; width: 300px; }
  .card--back .brand__square { width: 96px; height: 96px; }
  .card--back .brand__name { font-size: 22px; margin-top: 14px; }

  .card--front .brand { left: 46px; top: 42px; width: 210px; }
  .card--front .brand__square { width: 62px; height: 62px; border-radius: 6px; }
  .card--front .brand__name { font-size: 14px; margin-top: 9px; }

  /* Services on the back */
  .services { position: absolute; inset: 0; list-style: none; }
  .service {
    position: absolute; width: 180px; text-align: center;
    font-size: 12px; font-weight: 700; letter-spacing: 1px;
    color: var(--muted); text-transform: uppercase;
  }
  .service::after {
    content: ""; display: block; height: 7px; margin: 4px auto 0;
    width: 150px; border-radius: 4px;
    background: linear-gradient(90deg, transparent, var(--lime-soft) 15%, var(--lime-soft) 85%, transparent);
  }
  .service--l1 { left: 30px; top: 92px; }
  .service--l2 { left: 30px; top: 162px; }
  .service--l3 { left: 30px; top: 232px; }
  .service--l4 { left: 30px; top: 302px; }
  .service--r1 { left: 510px; top: 60px; }
  .service--r2 { left: 510px; top: 120px; }
  .service--r3 { left: 510px; top: 180px; }
  .service--r4 { left: 510px; top: 240px; }
  .service--r5 { left: 510px; top: 300px; }
  .service--c1 { left: 270px; top: 330px; }

  /* Front contact block */
  .contacts {
    position: absolute; left: 46px; top: 212px; list-style: none;
  }
  .contact {
    display: flex; align-items: center; gap: 12px;
    font-size: 12px; font-weight: 600; color: var(--white);
    height: 21px;
  }
  .contact svg { width: 14px; height: 14px; flex: none; }
  .divider {
    position: absolute; left: 388px; top: 200px;
    width: 2px; height: 140px; background: var(--lime);
  }
  .person { position: absolute; left: 420px; top: 262px; }
  .person__name {
    font-size: 26px; font-weight: 700; text-transform: uppercase;
    letter-spacing: 0.3px; line-height: 1;
  }
  .person__first { color: var(--white); }
  .person__last { color: var(--lime); }
  .person__role {
    font-size: 15px; font-weight: 600; color: var(--silver); line-height: 1.1;
  }
  .band {
    position: absolute; left: 0; right: 0; bottom: 14px;
    height: 9px; background: var(--lime);
  }
</style>
</head>
<body>
<main class="stage">

  <section class="card card--back" aria-label="Business card back">
    <ul class="services">
      <li class="service service--l1">Interior - Exterior</li>
      <li class="service service--l2">Special Effects</li>
      <li class="service service--l3">10 Year Guarantee</li>
      <li class="service service--l4">Fully Insured</li>
      <li class="service service--r1">Fully Qualified</li>
      <li class="service service--r2">Residential - Commercial</li>
      <li class="service service--r3">Pensioner Discount</li>
      <li class="service service--r4">Texture Coatings</li>
      <li class="service service--r5">Obligation Free Quotes</li>
      <li class="service service--c1">Water Damage Repair</li>
    </ul>
    <div class="brand">
      <span class="brand__square"></span>
      <span class="brand__name">Bramblewood Coatings Pty Ltd</span>
    </div>
  </section>

  <section class="card card--front" aria-label="Business card front">
    <div class="brand">
      <span class="brand__square"></span>
      <span class="brand__name">Bramblewood Coatings Pty Ltd</span>
    </div>

    <ul class="contacts">
      <li class="contact">
        <svg viewBox="0 0 14 14" aria-hidden="true"><rect x="3.5" y="1" width="7" height="12" rx="1.5" fill="none" stroke="var(--lime)" stroke-width="1.5"/><circle cx="7" cy="10.5" r="0.9" fill="var(--lime)"/></svg>
        +61 400 118 362
      </li>
      <li class="contact">
        <svg viewBox="0 0 14 14" aria-hidden="true"><rect x="1" y="3" width="12" height="8.5" fill="none" stroke="var(--lime)" stroke-width="1.5"/><path d="M1 3.5 L7 8 L13 3.5" fill="none" stroke="var(--lime)" stroke-width="1.5"/></svg>
        dean@bramblewoodcoatings.com.au
      </li>
      <li class="contact">
        <svg viewBox="0 0 14 14" aria-hidden="true"><path d="M3 1.5 L5.5 4 L4.2 5.8 Q5.8 8.6 8.2 9.8 L10 8.5 L12.5 11 L11 12.8 Q5 12 1.3 3 Z" fill="var(--lime)"/></svg>
        02 5550 7314
      </li>
      <li class="contact">
        <svg viewBox="0 0 14 14" aria-hidden="true"><path d="M7 13 C3 8 2.5 6.5 2.5 5 A4.5 4.5 0 0 1 11.5 5 C11.5 6.5 11 8 7 13 Z" fill="var(--lime)"/><circle cx="7" cy="5" r="1.6" fill="var(--card)"/></svg>
        PO Box 418, Bramblewood.
      </li>
      <li class="contact">
        <svg viewBox="0 0 14 14" aria-hidden="true"><circle cx="7" cy="7" r="5.5" fill="none" stroke="var(--lime)" stroke-width="1.5"/><path d="M1.5 7 H12.5 M7 1.5 C4.5 4.5 4.5 9.5 7 12.5 M7 1.5 C9.5 4.5 9.5 9.5 7 12.5" fill="none" stroke="var(--lime)" stroke-width="1.1"/></svg>
        www.bramblewoodcoatings.com.au
      </li>
    </ul>

    <div class="divider"></div>

    <div class="person">
      <p class="person__name"><span class="person__first">Dean</span><span class="person__last">Hollister</span></p>
      <p class="person__role">executive director</p>
    </div>

    <div class="band"></div>
  </section>

</main>
</body>
</html>
```